CODED website - Wanderfrom418

I am a successful entrepreneur - have recently sold my business and am semi-retired. I want to give something back, as well as provide a blog for articles and my journeys.

I will also be using this to provide free business and entrepreneurial advice.

I am creating a NOT FOR PROFIT business called Wanderfrom418.com.au which will provide the following;

1. Blog and articles; my travels, Small to Medium business advice and articles

2. My Bucket List - the 100 things I aim to achieve

3. Free business / start up advice - a section on the website which provides case studies on people / businesses which ask me for advice. We will then chronicle their story and what advice we have given for them to succeed.

My inspiration is the Marten Oskoby idea and website;

http://martenoskoby.com/about-marten/

Obviously I do NOT want a copy of this site, but use this for inspiration.

Furthermore, I would be interested in ongoing collaboration with the successful designer - I will be providing advice and consultancy to start ups, all of which will need web design etc, so there is ongoing referral streams for the successful designer.

I need this to be CODED and then uplifted to the website, so please DO NOT bid on this unless you can provide a coded site and facilitate the upload to BrightHostly.

The NECESSARY tabs / pages

Main landing page - a short introduction into the ethos of Wanderfrom418

Writing - this will be the blog articles

About

Our Bucket List - a section where we can add our 100 buket list items. Hyperlinked to open a new page which has details on each bucket list item (ie #1 Make Wanderfrom418 - hyperlink to a new page which then has info on the bucklist item and what we have done)

Wanderfrom418 - this will be the section where we discuss people / businesses that we are helping. We will have an opening intro section + a link to the contact us page so they can ask us for the free advice. This will be the section where we have case studies into businesses / people that we have helped.

Hey everyone!

I'm really keen to get this website launched and looking amazing - if you have any questions, or would like to discuss anything at all, please email me at

dane@pellorpost.com.au

As I mentioned in the brief, I am doing this site to give back; I will not be earning a cent, and I will not be trying to earn any funds. I'm doing it simply to help other start ups or entrepreneurs, so I really want this site to look amazing.

I hope someone reads this and is inspired, and wants to be involved in this social enterprise with me.

Really excited to hear from you all and see your designs!

Industry/Entity Type

Business

Requirements
Must have
• MUST BE CODED and uplifted to the BrightHostl registered domain - www.wanderfrom418.com.au - happy to discuss additional costings for this with successful designer.

Separate pages for each section (as outlined in the brief above)

Blog section to look similar to http://martenoskoby.com/3x5/

Comprehensive website - not a simple wordpress template theme with some minor modifications. I will immediately reject any simple template design. I am looking for a slick, fully functioning website design.

PLEASE BE AWARE that I am looking for ongoing collaboration with the www.wanderfrom418.com.au.

I am trying this website as I want to find a young, energetic, vibrant, dynamic designer - this is your opportunity to be a part of something big, as this website will be huge!

Please do not submit a design if you are not motivated and ready for something big.

```html
<!DOCTYPE html>
<html lang="en">
<head>
<meta charset="utf-8">
<title>Wanderfrom418.com.au</title>
<link rel="stylesheet" href="https://fonts.googleapis.com/css2?family=Exo:wght@600;700&family=Ubuntu:wght@400&display=swap">
<style>
:root{
  --page:#ecebe6;
  --panel:#ffffff;
  --ink:#2b2b2b;
  --body:#6b6b6b;
  --muted:#9a9a9a;
  --accent:#e0672e;
  --nav:#2d2d2d;
  --footer:#333333;
  --footer-base:#2a2a2a;
  --footer-line:#444444;
  --rule:#e6e6e6;
}
*{margin:0;padding:0;box-sizing:border-box}
html,body{width:1200px;height:2769px;overflow:hidden}
body{background:var(--page);font-family:Arial,Helvetica,sans-serif;color:var(--body);position:relative}
.abs{position:absolute}

.topbar{left:99px;top:0;width:1009px;height:42px;background:var(--panel)}
.topbar .dot{top:14px;width:18px;height:18px;border-radius:50%;background:#555}
.topbar .tagline{left:190px;top:14px;font-size:11px;font-style:italic;color:#b0b0b0;white-space:nowrap}
.topbar .account{right:12px;top:14px;font-size:11px;font-weight:bold;color:var(--ink);white-space:nowrap}
.topbar .account span{color:var(--accent)}

.brand{left:99px;top:92px;width:340px;height:90px;display:flex;align-items:center;gap:12px}
.brand .mark{width:22px;height:22px;border-radius:50%;background:var(--accent);flex:none}
.brand .name{font-family:Exo,sans-serif;font-weight:700;font-size:30px;color:var(--ink);line-height:1;white-space:nowrap}

.nav{top:95px;height:41px;display:flex;align-items:center;justify-content:center;background:var(--nav);color:#fff;font-family:Exo,sans-serif;font-weight:700;font-size:15px;letter-spacing:.5px;white-space:nowrap;text-decoration:none}
.nav.active{background:var(--accent)}

.panel{left:99px;top:219px;width:1009px;height:2015px;background:var(--panel)}

.h-section{font-family:Exo,sans-serif;font-weight:700;font-size:40px;color:var(--ink);letter-spacing:.5px;text-transform:uppercase;white-space:nowrap}
.hero{left:166px;top:358px;width:875px;height:674px;background:linear-gradient(180deg,#f5b82a 0%,#f2a11e 45%,#9b8a62 62%,#6f6f66 100%)}
.portrait{left:166px;top:1085px;width:319px;height:484px;background:linear-gradient(180deg,#f4f4f4 0%,#bcd6e6 45%,#9fc3d9 100%)}
.intro-name{left:510px;top:1102px;font-family:Ubuntu,sans-serif;font-size:44px;color:var(--ink);white-space:nowrap}
.intro-copy{left:510px;top:1166px;width:560px;font-size:12.5px;line-height:23px;color:var(--body)}

.rule{left:143px;width:922px;height:1px;background:var(--rule)}
.share{top:1589px;height:22px;border:1px solid #cfd6e2;border-radius:3px;background:#eef1f6;font-size:11px;color:#4a5a78;display:flex;align-items:center;justify-content:center;font-weight:bold}
.share-count{top:1589px;height:22px;border:1px solid #d5d5d5;border-radius:3px;background:#fff;font-size:11px;color:#666;display:flex;align-items:center;justify-content:center;width:26px}
.share-note{left:262px;top:1594px;font-size:11px;color:#555;white-space:nowrap}

.news-sub{left:143px;top:1748px;font-size:12.5px;color:var(--body)}
.thumb-a{left:152px;top:1805px;width:427px;height:272px;background:linear-gradient(180deg,#27384f 0%,#3a4a63 55%,#a46c2a 80%,#28303a 100%)}
.thumb-b{left:614px;top:1805px;width:427px;height:272px;background:linear-gradient(180deg,#3b4252 0%,#7b8598 45%,#b9c7d6 70%,#8ea3b8 100%)}
.article-title{top:2106px;width:427px;text-align:center;font-family:Exo,sans-serif;font-weight:700;font-size:26px;color:var(--ink)}
.article-excerpt{top:2153px;width:440px;font-size:12.5px;color:var(--body);white-space:nowrap}

.footer{left:0;top:2268px;width:1200px;height:432px;background:var(--footer)}
.footer-title{left:115px;top:2313px;font-family:Exo,sans-serif;font-weight:700;font-size:19px;color:var(--accent)}
.pager{top:2322px;width:10px;height:10px;border-radius:50%}
.post-thumb{width:143px;height:115px;border:3px solid #444}
.post-title{font-size:13px;font-weight:bold;color:#eee}
.post-meta{font-size:11px;font-style:italic;color:#999;white-space:nowrap}
.post-meta b{font-style:normal;color:#eee}

.base{left:0;top:2700px;width:1200px;height:69px;background:var(--footer-base);border-top:1px solid var(--footer-line)}
.base-link{left:99px;top:2731px;font-size:12px;color:#eee}
.base-copy{left:733px;top:2731px;font-size:11px;color:#999;white-space:nowrap}
.base-dot{top:2734px;width:10px;height:10px;border-radius:50%}
</style>
</head>
<body>

<header class="abs topbar">
  <span class="abs dot" style="left:39px"></span>
  <span class="abs dot" style="left:71px"></span>
  <span class="abs dot" style="left:103px"></span>
  <span class="abs dot" style="left:135px"></span>
  <span class="abs tagline">Donec at mattis erat! Duis sed massa eget eros gravida vulputate nec et ipsum.</span>
  <span class="abs account">LOGIN &nbsp;|&nbsp; <span>SIGN IN</span></span>
</header>

<div class="abs brand"><span class="mark"></span><span class="name">Wanderfrom418</span></div>

<nav>
  <a class="abs nav active" style="left:464px;width:90px">HOME</a>
  <a class="abs nav" style="left:565px;width:110px">WRITING</a>
  <a class="abs nav" style="left:686px;width:95px">ABOUT</a>
  <a class="abs nav" style="left:792px;width:140px">BUCKET LIST</a>
  <a class="abs nav" style="left:943px;width:165px">WANDERFROM418</a>
</nav>

<main class="abs panel"></main>

<h1 class="abs h-section" style="left:143px;top:258px">Welcome to Wanderfrom418.com.au</h1>
<div class="abs hero" role="img" aria-label="Sunset over the sea with a kangaroo leaping along the shore, framed with torn paper edges"></div>

<div class="abs portrait" role="img" aria-label="Portrait of the site owner in a light blue shirt"></div>
<h2 class="abs intro-name">Your name goes here</h2>
<p class="abs intro-copy">Curabitur blandit tempus porttitor. Nullam quis risus eget urna mollis ornare vel eu leo. Etiam porta sem malesuada magna mollis euismod. Aenean lacinia bibendum nulla sed consectetur. Duis mollis, est non commodo luctus, nisi erat porttitor ligula, eget lacinia odio sem nec elit. Vestibulum id ligula porta felis euismod semper. Vivamus sagittis lacus vel augue laoreet rutrum faucibus dolor auctor. Nulla vitae elit libero, a pharetra augue. Duis mollis, est non commodo luctus, nisi erat porttitor ligula, eget lacinia odio sem nec elit fermentum. Vestibulum id ligula porta felis euismod semper. Nullam quis risus eget urna mollis ornare vel eu leo. Lorem ipsum dolor sit amet, consectetur adipiscing elit. Maecenas faucibus mollis interdum. Etiam porta sem malesuada magna mollis euismod. Aenean lacinia bibendum nulla sed consectetur. Duis mollis, est non commodo luctus, nisi erat porttitor ligula, eget lacinia odio sem nec elit. Fusce dapibus, tellus ac cursus commodo, tortor mauris condimentum nibh, ut fermentum massa justo sit amet risus. Vestibulum id ligula porta felis euismod semper.</p>

<div class="abs rule" style="top:1573px"></div>
<span class="abs share" style="left:143px;width:50px">Like</span>
<span class="abs share" style="left:200px;width:55px">Send</span>
<span class="abs share-note">Be the first of your friends to like this.</span>
<span class="abs share" style="left:567px;width:36px;background:#f4f4f4;border-color:#ddd;color:#555">+1</span>
<span class="abs share-count" style="left:608px">0</span>
<span class="abs share" style="left:665px;width:64px;background:#f4f4f4;border-color:#ddd;color:#555">Share</span>
<span class="abs share-count" style="left:734px">0</span>
<span class="abs share" style="left:773px;width:64px;background:#eef6fb;border-color:#c9dfec;color:#3a6d8c">Tweet</span>
<span class="abs share-count" style="left:842px">0</span>
<span class="abs share" style="left:893px;width:42px;background:#fff;border-color:#d9b3b3;color:#b33">Pin</span>
<div class="abs rule" style="top:1661px"></div>

<h2 class="abs h-section" style="left:143px;top:1692px">Latest Wanderfrom418 News</h2>
<p class="abs news-sub">Pellentesque tristique tellus tristique leo rutrum ut dapibus.</p>

<div class="abs thumb-a" role="img" aria-label="Suspension bridge lit at night under a moonlit sky"></div>
<div class="abs thumb-b" role="img" aria-label="Old pier posts standing in calm water at dusk"></div>
<h3 class="abs article-title" style="left:152px">ARTICLE #2-2</h3>
<h3 class="abs article-title" style="left:614px">ARTICLE #1-2</h3>
<p class="abs article-excerpt" style="left:145px">One of the most iconic series in the history of games, Relic Runner is...</p>
<p class="abs article-excerpt" style="left:609px">Sed a velit vitae nunc porta iaculis. Aliquam tempus rutrum diam, non...</p>

<footer class="abs footer"></footer>
<h4 class="abs footer-title">LATEST BLOG ARTICLES</h4>
<span class="abs pager" style="left:1055px;background:var(--accent)"></span>
<span class="abs pager" style="left:1068px;background:#777"></span>

<div class="abs post-thumb" style="left:115px;top:2368px;background:linear-gradient(180deg,#6d6f8a,#c4a5a5 55%,#3e5360)" role="img" aria-label="Pier stretching into a pastel sea"></div>
<span class="abs post-title" style="left:277px;top:2373px">Article #2-3</span>
<span class="abs post-meta" style="left:277px;top:2401px">December 29, 2012 &nbsp; <b>No comments</b></span>

<div class="abs post-thumb" style="left:605px;top:2368px;background:linear-gradient(180deg,#5b6b86,#d39a6a 55%,#4a3f3a)" role="img" aria-label="Rock arch on a beach at sunset"></div>
<span class="abs post-title" style="left:766px;top:2373px">Article #1-3</span>
<span class="abs post-meta" style="left:766px;top:2401px">December 29, 2012 &nbsp; <b>No comments</b></span>

<div class="abs post-thumb" style="left:115px;top:2513px;background:linear-gradient(180deg,#8a9fb3,#d7b78e 55%,#5d4a3b)" role="img" aria-label="Rocky coastline in warm light"></div>
<span class="abs post-title" style="left:277px;top:2518px">Article #1</span>
<span class="abs post-meta" style="left:277px;top:2546px">December 29, 2012 &nbsp; <b>No comments</b></span>

<div class="abs post-thumb" style="left:605px;top:2513px;background:linear-gradient(180deg,#3c3550,#c4505a 55%,#2f2b35)" role="img" aria-label="Bridge against a red evening sky"></div>
<span class="abs post-title" style="left:766px;top:2518px">Article #2</span>
<span class="abs post-meta" style="left:766px;top:2546px">December 29, 2012 &nbsp; <b>No comments</b></span>

<div class="abs base"></div>
<a class="abs base-link">Sitemap</a>
<span class="abs base-copy">Copyright © Wanderfrom418.com.au - All rights reserved.</span>
<span class="abs base-dot" style="left:1057px;background:var(--accent)"></span>
<span class="abs base-dot" style="left:1073px;background:#888"></span>
<span class="abs base-dot" style="left:1089px;background:#d9453a"></span>

</body>
</html>
```